Kettle Past Noon - Book cover for collection of odd short stories

We need a book cover for ebook and print versions for an anthology of short stories. The title "Kettle Past Noon" relates to stories with something odd or not-quite-right about them. The attached photo is an example of a carpenter level, the idea is the level would appear perfectly level, but the bubble would be off-center. "Stories by: Moira Tesslund, Janet Orloff, Rob T. Vessey, Author, Author". Other creative elements could be wildly improbable things, e.g. pig's flying, hell freezing, etc. We prefer an uncluttered cover, however. Licenses included or unnecessary, delivery files must be fully compatible with Adobe Illustrator, with all layers intact.

Target Market(s)

People who like short stories with odd overtones or twist endings.

Industry/Entity Type

Book Publisher

Font styles to use
Serif

Colors

Designer to choose colors to be used in the design.

Requirements
Must have
• Incorporation of the concept, Kettle Past Noon
Nice to have
• Other ways to show the same meaning

```html
<!DOCTYPE html>
<html lang="en">
<head>
<meta charset="utf-8">
<title>Kettle Past Noon – Cover Spread</title>
<link rel="stylesheet" href="https://fonts.googleapis.com/css2?family=Poppins:wght@300;400;600;700&display=swap">
<style>
  :root {
    --backdrop: #000000;
    --paper: #ffffff;
    --title-grey: #858383;
    --body-grey: #9a9a9a;
    --byline-grey: #737171;
    --level-yellow: #f7d21e;
    --level-deep: #e3b70c;
    --guide: #b9b9b9;
    --press-green: #1f5e3a;
  }
  * { margin: 0; padding: 0; box-sizing: border-box; }
  html, body { width: 1200px; height: 922px; overflow: hidden; background: var(--backdrop); }
  body { position: relative; font-family: "Poppins", sans-serif; }

  .spread { position: absolute; left: 38px; top: 48px; width: 1122px; height: 797px; background: var(--paper); overflow: hidden; }
  .trim { position: absolute; border: 1px dashed var(--guide); pointer-events: none; }
  .trim--back { left: 13px; top: 10px; width: 507px; height: 776px; }
  .trim--spine { left: 530px; top: -2px; width: 63px; height: 800px; border-top: none; border-bottom: none; }
  .trim--front { left: 604px; top: 10px; width: 507px; height: 776px; }

  .level { position: absolute; background: linear-gradient(180deg, var(--level-yellow), var(--level-deep)); box-shadow: 0 12px 18px rgba(0,0,0,0.18); }
  .level--back { left: 60px; top: 274px; width: 116px; height: 530px; border-radius: 6px 6px 0 0; background: linear-gradient(90deg, var(--level-deep), var(--level-yellow) 40%, var(--level-deep)); box-shadow: -12px 10px 18px rgba(0,0,0,0.15); }
  .level--front { left: 620px; top: 96px; width: 510px; height: 142px; border-radius: 6px 0 0 6px; }

  .vertical { position: absolute; writing-mode: vertical-rl; white-space: nowrap; line-height: 1; }
  .back-title { left: 94px; top: 48px; font-weight: 700; font-size: 38px; line-height: 36px; }
  .back-title .line { display: block; }
  .grey { color: var(--title-grey); }
  .yellow { color: var(--level-yellow); }

  .blurb { position: absolute; left: 201px; top: 46px; width: 310px; font-weight: 600; font-size: 16.5px; line-height: 31.2px; color: var(--body-grey); letter-spacing: -0.2px; }
  .review { position: absolute; left: 199px; top: 644px; color: var(--title-grey); }
  .review__quote { font-weight: 300; font-size: 21px; line-height: 22.5px; }
  .review__source { margin-top: 8px; font-weight: 400; font-size: 13.5px; }

  .spine-title { left: 581px; top: 52px; font-size: 33px; }
  .spine-title .bold { font-weight: 700; }
  .spine-title .light { font-weight: 300; color: var(--title-grey); }
  .spine-title .gap { display: inline-block; height: 12px; }

  .press { position: absolute; left: 531px; top: 682px; width: 62px; text-align: center; }
  .press__mark { display: block; width: 26px; height: 26px; margin: 0 auto 6px; background: var(--press-green); }
  .press__name { font-weight: 600; font-size: 8.5px; line-height: 10px; color: var(--title-grey); }

  .front-title { position: absolute; left: 642px; top: 322px; width: 420px; text-align: center; font-weight: 700; font-size: 106px; line-height: 88px; letter-spacing: -2px; }
  .front-title .line { display: block; }
  .byline { position: absolute; left: 622px; top: 656px; width: 460px; text-align: center; font-weight: 600; font-size: 21.5px; line-height: 25.5px; color: var(--byline-grey); }
</style>
</head>
<body>
  <main class="spread">
    <!-- Back cover -->
    <div class="vertical back-title">
      <span class="line grey">Kettle</span>
      <span class="line yellow">Past Noon</span>
    </div>
    <div class="level level--back" role="img" aria-label="Photo of a yellow carpenter's level standing upright, its bubbles sitting off-centre"></div>
    <p class="blurb">Nibh vel velit auctor aliquet. Aenean sollicitudin, lorem quis bibendum auctor, nisi elit consequat ipsum, nec sagittis sem nibh id elit. Duis sed odio sit amet nibh vulputate cursus a sit amet mauris. Morbi accumsan ipsum velit. Nam nec tellus a odio tincidunt auctor a ornare odio. Sed non mauris vitae erat consequat auctor eu in elit. Class aptent taciti sociosqu ad litora torquent per conubia nostra, per inceptos himenaeos. Mauris in erat justo. Nullam ac cursus condimentum sit amet a augue. Sed non neque elit. Sed ut imperdiet nisi. Proin tellus a odio.</p>
    <div class="review">
      <p class="review__quote">Alluringly<br>strange<br>collection<br>of musings</p>
      <p class="review__source">Book review quote</p>
    </div>

    <!-- Spine -->
    <div class="vertical spine-title">
      <span class="bold grey">Kettle</span><span class="gap"></span><span class="bold yellow">Past Noon</span><span class="gap"></span><span class="light">Short Stories</span>
    </div>
    <div class="press">
      <span class="press__mark"></span>
      <p class="press__name">Stray Lantern<br>Press</p>
    </div>

    <!-- Front cover -->
    <div class="level level--front" role="img" aria-label="Photo of a yellow carpenter's level lying flat, its bubbles sitting off-centre"></div>
    <h1 class="front-title">
      <span class="line grey">Kettle</span>
      <span class="line yellow">Past</span>
      <span class="line yellow">Noon</span>
    </h1>
    <p class="byline">An Anthology of Short Stories<br>by Moira Tesslund,<br>Janet Orloff, Rob T. Vessey and others</p>

    <div class="trim trim--back"></div>
    <div class="trim trim--spine"></div>
    <div class="trim trim--front"></div>
  </main>
</body>
</html>
```